Beautiful Quotes For Social Media Posts

We are looking for 5 beautifully designed quotes for our social media account.

Inspiration of styles we like in both style and color along with a few of our favorite fonts (you are NOT limited to these fonts this is just to give you an idea):
https://quillmorestudio.example.com/s/k7p2vx9tqa41mzn8wbd3ce6hr5lf0y2j

*These fonts are property of Quillmore Studio. You do not have permission/rights to use them outside of this assignment*

Quotes to use (5):
“Only those who dare to fail greatly can ever achieve greatly.” –Vernon T. Ashgrove
“Don’t go through life, grow through life.” – Milo Pendrake
“Follow your bliss and the universe will open doors where there were only walls.” – Arthur Venholm
“If you don’t like the road you’re walking, start paving another one.” – Greta Mossley
“Life is like riding a bicycle. To keep your balance, you must keep moving.” —Lucian Thornwick

File Specifics:
- JPG
- 10x10 in size (square)
- Please include @QuillmoreStudio in the bottom right left or center of each design

Brand Details:
Soft but rich pastel and bright colors.
Hand Drawn florals, doodles and art
Handwritten looking fonts
Artsy, Creative, Girl and Inspiring

```html
<!DOCTYPE html>
<html lang="en">
<head>
<meta charset="utf-8">
<title>Quote Post – Paving Another Road</title>
<link href="https://fonts.googleapis.com/css2?family=Oswald:wght@400&family=Dancing+Script:wght@500&family=Mr+Dafoe&display=swap" rel="stylesheet">
<style>
  :root {
    --stage: #d3d3d3;
    --blush-light: #fde8f0;
    --blush-deep: #f8d5e3;
    --circle: #ffffff;
    --ink: #1d1d1d;
    --orchid: #a0449b;
    --petal-pink: #eab0cf;
    --petal-rose: #d987b8;
    --petal-violet: #c3a8de;
    --leaf: #c4dfc6;
  }
  * { margin: 0; padding: 0; box-sizing: border-box; }
  html, body {
    width: 741px;
    height: 1200px;
    overflow: hidden;
    background: var(--stage);
  }
  .quote-post {
    position: absolute;
    left: 20px;
    top: 250px;
    width: 700px;
    height: 700px;
    background: radial-gradient(circle at 50% 50%, var(--blush-light) 0%, var(--blush-deep) 100%);
    box-shadow: 0 10px 24px rgba(0,0,0,0.18);
    overflow: hidden;
  }
  .wreath {
    position: absolute;
    inset: 0;
  }
  .quote {
    position: absolute;
    left: 160px;
    top: 0;
    width: 380px;
    height: 700px;
    text-align: center;
    color: var(--ink);
  }
  .quote-line {
    position: absolute;
    left: 0;
    width: 100%;
    font-family: "Dancing Script", cursive;
    font-size: 22px;
    font-weight: 500;
    font-style: italic;
    line-height: 1;
    white-space: nowrap;
  }
  .quote-line--first { top: 290px; }
  .quote-line--last { top: 370px; }
  .quote-mark {
    font-family: Georgia, serif;
    font-weight: 700;
    font-size: 24px;
  }
  .quote-highlight {
    position: absolute;
    left: 0;
    width: 100%;
    top: 314px;
    font-family: "Oswald", sans-serif;
    font-size: 44px;
    line-height: 1.2;
    color: var(--orchid);
    white-space: nowrap;
  }
  .quote-author {
    position: absolute;
    top: 422px;
    left: 0;
    width: 100%;
    padding-right: 76px;
    text-align: right;
    font-family: "Mr Dafoe", cursive;
    font-size: 21px;
    line-height: 1;
    color: var(--ink);
  }
  .studio-handle {
    position: absolute;
    right: 22px;
    bottom: 16px;
    font-family: "Oswald", sans-serif;
    font-size: 14px;
    letter-spacing: 0.5px;
    color: var(--orchid);
  }
</style>
</head>
<body>
  <main class="quote-post">
    <svg class="wreath" viewBox="0 0 700 700" width="700" height="700">
      <defs>
        <radialGradient id="wreath-tone" cx="50%" cy="50%" r="50%">
          <stop offset="50%" stop-color="#e6a6c9"/>
          <stop offset="66%" stop-color="#eab0cf"/>
          <stop offset="80%" stop-color="#d7bde3"/>
          <stop offset="92%" stop-color="#cfe3cf" stop-opacity="0.7"/>
          <stop offset="100%" stop-color="#f8d5e3" stop-opacity="0"/>
        </radialGradient>
        <filter id="soft-edge" x="-10%" y="-10%" width="120%" height="120%">
          <feGaussianBlur stdDeviation="6"/>
        </filter>
        <filter id="soft-shadow" x="-10%" y="-10%" width="120%" height="120%">
          <feDropShadow dx="0" dy="3" stdDeviation="5" flood-color="#b07b93" flood-opacity="0.35"/>
        </filter>
      </defs>
      <ellipse role="img" aria-label="Watercolour wreath of pink gerberas, roses, violet daisies and green leaves"
               cx="347" cy="350" rx="272" ry="336" fill="url(#wreath-tone)" filter="url(#soft-edge)"/>
      <circle class="quote-circle" cx="347" cy="352" r="188" fill="var(--circle)" filter="url(#soft-shadow)"/>
    </svg>

    <div class="quote">
      <p class="quote-line quote-line--first"><span class="quote-mark">“</span>If you don’t like the road</p>
      <p class="quote-highlight">you’re walking,</p>
      <p class="quote-line quote-line--last">start paving another one.<span class="quote-mark">”</span></p>
      <p class="quote-author">– Greta Mossley</p>
    </div>

    <p class="studio-handle">@QuillmoreStudio</p>
  </main>
</body>
</html>
```